Etiketten für Olivenöl-Intensivcreme
Zielgruppe
Wir produzieren Bio-Food, u.a. Wein und Olivenöl. Jetzt soll eine Olivenöl-Intensivcreme im Bereich Kosmetik auf dem Markt platziert werden. Unsere Zielgruppe hat ein sehr breites Altersspektrum (jung bis alt), ist naturverbunden, tierlieb, gebildet, kritisch-reflektierend, weiß gute Qualität zu schätzen, ist überwiegend weiblich. Die Olivenöl-Intensivcreme hat eine sehr breite Verwendung und soll sich als 'Allzweckwaffe' in jedem Haushalt etablieren (Babyhaut-Pflege, Lippenpflege, Ganzkörperpflege, Hand-Schutzcreme etc.).
Aufgabenstellung
Die Creme soll heißen: Tavunel (es könnte z.B. der Buchstabe 'O' durch eine Olive ersetzt werden). Es gibt zwei Etikette (Deckeloberseite der Metalldose und auf dem Boden). Der Durchmesser der Etikette ist jeweils 5,5 cm. Die Deckelunterseite gilt reinen Pflichtangaben. Im Dateidownloadbereich sind die Textvorgaben für die Etikette. MUT zur Farbe! Wir sind NICHT brav und angepasst! Orange kann Akzente setzen bzw. für Aufmerksamkeit im Regal sorgen.

```html
<!DOCTYPE html>
<html lang="de">
<head>
<meta charset="utf-8">
<title>Tavunel – Olivenöl-Intensivcreme Etikett</title>
<link rel="stylesheet" href="https://fonts.googleapis.com/css2?family=Baloo+2:wght@700&family=Signika:wght@500&display=swap">
<style>
  :root {
    --page-bg: #efedea;
    --label-top: #f1eaa6;
    --label-mid: #f8f4cf;
    --label-bottom: #fffef6;
    --gold: #b8972a;
    --gold-light: #dcc46a;
    --gold-deep: #9c7c18;
    --text-olive: #5b6150;
  }
  html, body {
    margin: 0;
    padding: 0;
    width: 1200px;
    height: 1200px;
    overflow: hidden;
    background: var(--page-bg);
  }
  .canvas {
    position: relative;
    width: 1200px;
    height: 1200px;
  }
  .label-art {
    position: absolute;
    inset: 0;
  }
  .label-text {
    position: absolute;
    left: 0;
    width: 1200px;
    margin: 0;
    text-align: center;
  }
  .product-name {
    top: 218px;
    font-family: "Baloo 2", sans-serif;
    font-weight: 700;
    font-size: 128px;
    line-height: 1;
    letter-spacing: 2px;
    color: var(--gold);
  }
  .product-type {
    top: 360px;
    font-family: "Signika", sans-serif;
    font-weight: 500;
    font-size: 38px;
    line-height: 1;
    color: var(--text-olive);
  }
  .product-claims {
    top: 432px;
    font-family: "Signika", sans-serif;
    font-weight: 500;
    font-size: 36px;
    line-height: 43px;
    color: var(--text-olive);
    list-style: none;
    padding: 0;
  }
  .brand-name {
    top: 940px;
    font-family: "Signika", sans-serif;
    font-weight: 500;
    font-size: 36px;
    line-height: 1;
    letter-spacing: 1px;
    color: var(--gold);
  }
</style>
</head>
<body>
<main class="canvas">
  <svg class="label-art" width="1200" height="1200" viewBox="0 0 1200 1200" aria-hidden="false">
    <defs>
      <linearGradient id="labelFill" x1="0" y1="0" x2="0" y2="1">
        <stop offset="0" stop-color="var(--label-top)"/>
        <stop offset="0.5" stop-color="var(--label-mid)"/>
        <stop offset="1" stop-color="var(--label-bottom)"/>
      </linearGradient>
      <linearGradient id="branchFill" x1="0" y1="0" x2="1" y2="1">
        <stop offset="0" stop-color="var(--gold-light)"/>
        <stop offset="0.5" stop-color="var(--gold)"/>
        <stop offset="1" stop-color="var(--gold-deep)"/>
      </linearGradient>
      <clipPath id="labelClip">
        <circle cx="600" cy="600" r="470"/>
      </clipPath>
    </defs>

    <circle class="label-disc" cx="600" cy="600" r="470" fill="url(#labelFill)"/>

    <g clip-path="url(#labelClip)">
      <path class="olive-branch-left" role="img" aria-label="Goldener Olivenzweig mit Oliven und Blättern, links"
            d="M130 575 C260 570 380 640 470 700 C530 735 545 740 540 760 C470 790 420 800 400 860 C380 910 330 940 250 950 L130 950 Z"
            fill="url(#branchFill)" opacity="0.85"/>
      <path class="olive-branch-right" role="img" aria-label="Goldener Olivenzweig mit Oliven und Blättern, rechts"
            d="M1070 575 C940 580 830 650 740 705 C700 730 690 745 700 760 C760 790 790 820 800 870 C815 920 860 945 950 950 L1070 950 Z"
            fill="url(#branchFill)" opacity="0.85"/>
      <rect class="brand-emblem" role="img" aria-label="Goldene Illustration eines galoppierenden Pferdes"
            x="548" y="715" width="110" height="180" rx="24"
            fill="var(--gold-light)" opacity="0.55"/>
    </g>

    <circle class="label-edge" cx="600" cy="600" r="470" fill="none" stroke="var(--gold)" stroke-width="3"/>
  </svg>

  <h1 class="label-text product-name">Tavunel</h1>
  <p class="label-text product-type">Olivenöl-Intensivcreme</p>
  <ul class="label-text product-claims">
    <li>Naturkosmetik</li>
    <li>Bio-Olive</li>
    <li>vegan</li>
    <li>Pflege- und Schutzcreme</li>
  </ul>
  <p class="label-text brand-name">KORAVEL.LAND</p>
</main>
</body>
</html>
```